Korvane Business Cards

We need a business card design. We are a Technology (Audio Visual) design, sales and installation company. Looking for a double sided design, clean

Contact Information for Business Card

Clean, modern look, 2 sided

Font styles to use
Sans Serif

```html
<!DOCTYPE html>
<html lang="en">
<head>
<meta charset="utf-8">
<title>Korvane Business Cards</title>
<link rel="stylesheet" href="https://fonts.googleapis.com/css2?family=Montserrat:wght@500;600;800&family=Roboto:wght@400;500&display=swap">
<style>
  :root {
    --bg: #e9e9ea;
    --paper: #ffffff;
    --ink: #1b2a36;
    --text: #3a3f45;
    --accent: #f39a1e;
    --rule: #7d848c;
    --dark-1: #1f1f20;
    --dark-2: #3a3a3b;
    --dark-3: #8a8a8b;
  }
  * { box-sizing: border-box; margin: 0; padding: 0; }
  html, body { width: 1200px; height: 801px; overflow: hidden; }
  body {
    background: var(--bg);
    font-family: "Roboto", Arial, sans-serif;
    position: relative;
  }
  .card {
    position: absolute;
    top: 252px;
    width: 520px;
    height: 297px;
    border-bottom: 4px solid var(--accent);
    box-shadow: 0 10px 28px rgba(0,0,0,0.16);
  }
  .card--front { left: 50px; background: var(--paper); }
  .card--back { left: 630px; background: var(--dark-1); overflow: hidden; }

  .brand {
    position: absolute;
    left: 0; top: 0;
    width: 270px; height: 100%;
    display: flex; align-items: center; justify-content: center;
  }
  .brand__name {
    font-family: "Montserrat", Arial, sans-serif;
    font-weight: 800;
    font-size: 44px;
    letter-spacing: -1px;
    color: var(--ink);
  }
  .divider {
    position: absolute;
    left: 278px; top: 92px;
    width: 1px; height: 112px;
    background: var(--rule);
  }
  .details {
    position: absolute;
    left: 300px; top: 78px;
    color: var(--text);
    font-size: 12.5px;
    line-height: 1.35;
  }
  .details__name {
    font-family: "Montserrat", Arial, sans-serif;
    font-weight: 600;
    font-size: 17px;
    letter-spacing: 0.3px;
    text-transform: uppercase;
    color: var(--accent);
  }
  .details__role { font-size: 14px; margin-bottom: 8px; }
  .details__address { margin-bottom: 8px; }
  .contact { list-style: none; }
  .contact li { display: flex; align-items: center; gap: 8px; }
  .contact svg { width: 11px; height: 11px; flex: none; }
  .contact .hl { color: var(--accent); }

  .back-pattern {
    position: absolute; inset: 0;
    background: linear-gradient(120deg, var(--dark-1) 0%, var(--dark-2) 45%, var(--dark-3) 100%);
  }
  .back-name {
    position: absolute;
    right: 70px; top: 170px;
    font-family: "Montserrat", Arial, sans-serif;
    font-weight: 800;
    font-size: 30px;
    color: var(--accent);
  }
</style>
</head>
<body>
  <section class="card card--front" aria-label="Business card front">
    <div class="brand"><span class="brand__name">Korvane</span></div>
    <div class="divider"></div>
    <div class="details">
      <p class="details__name">Daniel Reyes</p>
      <p class="details__role">Manager</p>
      <p class="details__address">Your address, city<br>state, ZIP 0000</p>
      <ul class="contact">
        <li>
          <svg viewBox="0 0 12 12"><path d="M3 1l2 2.4-1.2 1.2a6 6 0 0 0 3.6 3.6L8.6 7 11 9l-1.4 2C5 11 1 7 1 2.4z" fill="var(--accent)"/></svg>
          <span>123-456-2100</span>
        </li>
        <li>
          <svg viewBox="0 0 12 12"><rect x="1" y="2.5" width="10" height="7" fill="none" stroke="var(--accent)" stroke-width="1.3"/><path d="M1 3l5 3.5L11 3" fill="none" stroke="var(--accent)" stroke-width="1.3"/></svg>
          <span>youremail@mailbox.com</span>
        </li>
        <li>
          <svg viewBox="0 0 12 12"><circle cx="6" cy="6" r="5" fill="var(--accent)"/><path d="M1 6h10M6 1c-2 2.5-2 7.5 0 10M6 1c2 2.5 2 7.5 0 10" fill="none" stroke="#fff" stroke-width="0.8"/></svg>
          <span>www.<span class="hl">yourwebsite</span>.com</span>
        </li>
      </ul>
    </div>
  </section>

  <section class="card card--back" aria-label="Business card back">
    <div class="back-pattern" role="img" aria-label="Repeating embossed letter pattern in dark grey fading to light grey"></div>
    <span class="back-name">Korvane</span>
  </section>
</body>
</html>
```